Passenger Balloon Flight Experience needs DL Flyer

We need a colourful flyer to promote our passenger balloon flight experience "Ember Valley Skyrides". The vertical DL 100 x 210mm flyer will sit in a brochure display with other DL brochures so the top 60-80mm is visible and must invite attention. We want to feature the "kanketsu.jpg" photo or a crop of it which is included in the uploaded files - this is the photo with the rugged mountain range in the background.
The text we'd like is in a file called text.docx - copy can be modified if recommended. We've also uploaded our logo (TealMark) that needs the phone number updated to 1300 847 392. Also uploaded are some other photos that could form part of the design.

Target Market(s)

Couples

Font styles to use
Sans Serif

Requirements
Must have
• Must inspire confidence in our safety and professionalism

```html
<!DOCTYPE html>
<html lang="en">
<head>
<meta charset="utf-8">
<title>Ember Valley Skyrides – DL Flyer</title>
<link rel="stylesheet" href="https://fonts.googleapis.com/css2?family=Poppins:wght@400;600&family=Roboto+Condensed:wght@400&display=swap">
<style>
  :root {
    --sky-top: #c9c4cf;
    --sky-low: #a79a9f;
    --range: #8a5a48;
    --foreground: #3e3a2a;
    --title-light: #ffffff;
    --ink: #1b1b1b;
    --paper: #ffffff;
    --band-yellow: #f7e600;
  }
  * { margin: 0; padding: 0; box-sizing: border-box; }
  html, body { width: 1200px; height: 2516px; overflow: hidden; background: var(--paper); }
  .flyer {
    position: relative; width: 1200px; height: 2516px;
    font-family: "Poppins", Arial, sans-serif; color: var(--ink);
  }
  .hero-photo {
    position: absolute; left: 0; top: 0; width: 1200px; height: 928px;
    background: linear-gradient(180deg,
      var(--sky-top) 0%, var(--sky-low) 14%, #9b7668 22%,
      var(--range) 34%, #6f4c3a 55%, #55493a 72%, var(--foreground) 100%);
  }
  .brand-title {
    position: absolute; left: 500px; top: 470px; width: 680px;
    font-family: "Poppins", Arial, sans-serif; font-weight: 600;
    color: var(--title-light);
    font-size: 104px; line-height: 114px;
  }
  .headlines {
    position: absolute; left: 0; top: 990px; width: 1200px;
    text-align: center; font-weight: 600; font-size: 56px; line-height: 70px;
  }
  .headlines p { margin-bottom: 46px; }
  .body-copy {
    font-family: "Roboto Condensed", "Arial Narrow", sans-serif;
    font-weight: 400; font-size: 42px; line-height: 50px;
  }
  .intro { position: absolute; left: 70px; top: 1620px; width: 1080px; }
  .details { position: absolute; left: 70px; top: 1790px; width: 420px; }
  .details p { margin-bottom: 50px; }
  .brand-mark {
    position: absolute; left: 540px; top: 1900px; width: 620px;
    display: flex; flex-direction: column; align-items: center; gap: 24px;
    font-family: "Poppins", Arial, sans-serif; font-weight: 600; color: var(--ink);
  }
  .brand-mark .name { display: flex; align-items: center; gap: 24px; font-size: 84px; line-height: 1; }
  .brand-mark .dot { width: 48px; height: 48px; border-radius: 50%; background: var(--ink); }
  .brand-mark .phone { font-size: 56px; line-height: 1; }
  .contact {
    position: absolute; left: 0; top: 2296px; width: 1200px;
    text-align: center; font-weight: 600; font-size: 44px; line-height: 56px;
  }
  .bottom-band {
    position: absolute; left: 0; top: 2432px; width: 1200px; height: 84px;
    background: var(--band-yellow);
  }
</style>
</head>
<body>
<main class="flyer">
  <div class="hero-photo" role="img" aria-label="Photograph of a rugged mountain range at dawn with a colourful striped hot-air balloon floating above the valley"></div>
  <h1 class="brand-title">Ember<br>Valley<br>Skyrides</h1>

  <section class="headlines">
    <p>See Victoria’s High Country.</p>
    <p>Beautiful Alpine scenery.</p>
    <p>A glorious sense of freedom<br>and adventure.</p>
    <p>The best way to experience it all<br>is by hot-air balloon!</p>
  </section>

  <p class="intro body-copy">Live the romance and adventure of a hot-air balloon flight in the Victorian High Country over Mansfield district at dawn.</p>

  <section class="details body-copy">
    <p>Take in the beautiful scenery, and awaken to a new perspective.</p>
    <p>We top off the experience with a delicious champagne breakfast after the flight.</p>
  </section>

  <div class="brand-mark">
    <div class="name"><span class="dot"></span>TealMark</div>
    <div class="phone">1300 847 392</div>
  </div>

  <p class="contact">Contact our friendly team for information<br>flights@tealmarkskyrides.com.au</p>

  <div class="bottom-band"></div>
</main>
</body>
</html>
```